out of the box Business Card Design for a Manufacturer / Distributor

We are a manufarturer and distributor of products.
the company name is VORTANI (Pic attached)

the picture is NOT a must have on the business Card.

the Business Card should look really professional and/or special, so out of the box thinking is welcome.

there should be 2 Adresses on the Business Card for Main and Branch Office.
Email Adress, homepage, Name is required
NO Phone Number

Our working field:
Private Labeling
high Quality Production
direct distribution
warehousing
trademark registration
legal support

Main Office:
Kornblumenweg 14
08352 Burgstädt
Germany

Branch Office:
Daska Lane
Sialkot
Pakistan

Names:
Lukas Feldhaus (Owner)
Imran Qureshi (Owner)

Email:
lukas@vortani-example.com
imran@vortani-example.com

homepage:
vortani-example.com

Industry/Entity Type

Manufacturer Distributer

Contact Information for Business Card

Vortani

Requirements
Must have
• Names, both office Adresses, email, homepage
Should not have
• Phone Number

```html
<!DOCTYPE html>
<html lang="en">
<head>
<meta charset="utf-8">
<title>VORTANI Business Card</title>
<link rel="stylesheet" href="https://fonts.googleapis.com/css2?family=Open+Sans:wght@400;600;700&display=swap">
<style>
  :root {
    --page-bg: #e6e4e1;
    --card-white: #ffffff;
    --panel-light: #f1f1f1;
    --ink: #3a3a3a;
    --ink-soft: #555555;
    --band-dark: #3d3d3d;
    --band-darker: #2a2a2a;
    --rule: #8a8a8a;
  }
  * { box-sizing: border-box; margin: 0; padding: 0; }
  html, body {
    width: 1200px; height: 900px; overflow: hidden;
    background: var(--page-bg);
    font-family: "Open Sans", Arial, sans-serif;
    color: var(--ink);
  }
  .canvas {
    width: 1200px; height: 900px;
    display: flex; flex-direction: column; align-items: center; justify-content: center;
    gap: 40px;
  }
  .card {
    position: relative; width: 700px; height: 400px;
    background: var(--card-white);
    box-shadow: 0 6px 18px rgba(0,0,0,.18);
    overflow: hidden;
  }

  /* Front */
  .card--front { background: linear-gradient(135deg, #ffffff 0%, #f2f2f2 60%, #e9e9e9 100%); }
  .services { position: absolute; left: 120px; top: 52px; }
  .services__title { font-weight: 700; font-size: 19px; margin-bottom: 8px; }
  .services__list { list-style: none; font-size: 17px; color: var(--ink-soft); line-height: 1.55; }
  .services__list li { padding-left: 26px; position: relative; }
  .services__list li::before {
    content: ""; position: absolute; left: 4px; top: 9px;
    width: 9px; height: 9px; background: var(--ink); transform: rotate(45deg);
  }
  .services__rule { position: absolute; left: 140px; top: 236px; width: 460px; height: 2px; background: var(--rule); }
  .brand { position: absolute; display: flex; align-items: center; gap: 18px; }
  .brand__dot { border-radius: 50%; flex: none; }
  .brand__name { font-weight: 400; letter-spacing: 2px; line-height: 1; }
  .card--front .brand { left: 80px; top: 258px; }
  .card--front .brand__dot { width: 70px; height: 70px; background: var(--ink); }
  .card--front .brand__name { font-size: 88px; color: var(--ink); }

  /* Back */
  .card--back { background: var(--band-dark); }
  .back-shapes { position: absolute; inset: 0; }
  .contacts { position: absolute; left: 0; right: 0; display: flex; justify-content: center; }
  .contacts--people { top: 22px; }
  .contacts--offices { top: 272px; }
  .contact { width: 270px; font-size: 15px; color: var(--ink-soft); line-height: 1.45; }
  .contact--left { text-align: right; padding-right: 20px; }
  .contact--right { text-align: left; padding-left: 20px; border-left: 2px solid var(--rule); }
  .contact strong { color: var(--ink); font-weight: 700; }
  .contact .label { font-weight: 700; color: var(--ink); font-size: 16px; }
  .icon { width: 13px; height: 13px; vertical-align: -2px; fill: var(--ink); }
  .card--back .brand { left: 0; right: 0; top: 166px; justify-content: center; }
  .card--back .brand__dot { width: 62px; height: 62px; background: #ffffff; }
  .card--back .brand__name { font-size: 74px; color: #ffffff; }
</style>
</head>
<body>
<main class="canvas">

  <section class="card card--front" aria-label="Card front">
    <div class="services">
      <h2 class="services__title">Our working field</h2>
      <ul class="services__list">
        <li>Private Labeling</li>
        <li>high Quality Production</li>
        <li>direct distribution / warehousing</li>
        <li>trademark registration / legal support</li>
      </ul>
    </div>
    <div class="services__rule"></div>
    <div class="brand">
      <span class="brand__dot"></span>
      <span class="brand__name">VORTANI</span>
    </div>
  </section>

  <section class="card card--back" aria-label="Card back">
    <svg class="back-shapes" viewBox="0 0 700 400" aria-hidden="true">
      <polygon points="0,0 700,0 700,36 590,146 110,146 0,36" fill="var(--band-darker)"/>
      <polygon points="0,0 700,0 700,26 584,136 116,136 0,26" fill="var(--panel-light)"/>
      <polygon points="0,400 700,400 700,360 586,256 114,256 0,360" fill="var(--band-darker)"/>
      <polygon points="0,400 700,400 700,372 580,266 120,266 0,372" fill="var(--card-white)"/>
    </svg>

    <div class="contacts contacts--people">
      <div class="contact contact--left">
        Owner | <strong>LUKAS FELDHAUS</strong><br>
        lukas@vortani-example.com
        <svg class="icon" viewBox="0 0 16 16"><path d="M1 4h14v9H1z M1 4l7 5 7-5" fill="none" stroke="#3a3a3a" stroke-width="1.6"/></svg>
      </div>
      <div class="contact contact--right">
        <strong>IMRAN QURESHI</strong> | Owner<br>
        <svg class="icon" viewBox="0 0 16 16"><path d="M1 4h14v9H1z M1 4l7 5 7-5" fill="none" stroke="#3a3a3a" stroke-width="1.6"/></svg>
        imran@vortani-example.com
      </div>
    </div>

    <div class="brand">
      <span class="brand__dot"></span>
      <span class="brand__name">VORTANI</span>
    </div>

    <div class="contacts contacts--offices">
      <div class="contact contact--left">
        <span class="label">Main Office:</span>
        <svg class="icon" viewBox="0 0 16 16"><path d="M8 1a5 5 0 0 0-5 5c0 4 5 9 5 9s5-5 5-9a5 5 0 0 0-5-5zm0 7a2 2 0 1 1 0-4 2 2 0 0 1 0 4z"/></svg><br>
        Kornblumenweg 14<br>
        08352 Eichenbrück, Nordmark
      </div>
      <div class="contact contact--right">
        <svg class="icon" viewBox="0 0 16 16"><path d="M8 1a5 5 0 0 0-5 5c0 4 5 9 5 9s5-5 5-9a5 5 0 0 0-5-5zm0 7a2 2 0 1 1 0-4 2 2 0 0 1 0 4z"/></svg>
        <span class="label">Branch Office:</span><br>
        Daska Lane, Rahimpur, Sundara<br>
        <svg class="icon" viewBox="0 0 16 16"><circle cx="8" cy="8" r="6.5" fill="none" stroke="#3a3a3a" stroke-width="1.5"/><path d="M1.5 8h13M8 1.5c-3 3.5-3 9.5 0 13M8 1.5c3 3.5 3 9.5 0 13" fill="none" stroke="#3a3a3a" stroke-width="1.2"/></svg>
        vortani-example.com
      </div>
    </div>
  </section>

</main>
</body>
</html>
```